Spiritual Self Help Book Cover

I need a book cover that's extremely appealing to spiritual seekers, self-help/health and wellness fans. Mostly for women.
The book blends spirituality/mysticism with science for readers to understand how to optimize their health/body, emotional well-being, mental wellness, spiritual fulfillment, relationships, business and purpose in life. It infuses ancient and modern understanding of energy/frequency/quantum mechanics along with the science of chiropractic and psychology.
Book title: Weaving The Silver River
I'll attach some examples that are similar to what I like but I want something different and more extravagantly beautiful.
Please use the graphic of the Sri Yantra Mandala into the cover instead of this stock image one.
I'll need the book cover in all formats: paperback, hardcover, ebook and audiobook.
I'll provide the rest of the details, including publisher logo, synopsis, author photo/blurb and ISBN after I pick the final wniner.
Mostly women spiritual seekers, self-help readers, health/wellness enthusiasts

```html
<!DOCTYPE html>
<html lang="en">
<head>
<meta charset="utf-8">
<title>Weaving The Silver River — Cover</title>
<link rel="stylesheet" href="https://fonts.googleapis.com/css2?family=Playfair+Display:wght@400;500&family=Inter:wght@700;800&display=swap">
<style>
  :root {
    --stage: #c96a4b;
    --paper: #f4f3f4;
    --ink: #1f1516;
    --pink: rgba(226, 122, 170, 0.75);
    --rose: rgba(232, 150, 180, 0.55);
    --lime: rgba(190, 214, 120, 0.85);
    --sun: rgba(240, 226, 120, 0.8);
    --amber: rgba(240, 170, 90, 0.75);
    --sky: rgba(130, 196, 214, 0.75);
    --lilac: rgba(170, 160, 220, 0.55);
  }
  * { margin: 0; padding: 0; box-sizing: border-box; }
  html, body {
    width: 1200px; height: 947px; overflow: hidden;
    background: var(--stage);
  }
  .stage {
    width: 1200px; height: 947px;
    display: flex; align-items: center; justify-content: center;
  }
  .cover {
    position: relative;
    width: 592px; height: 880px;
    background: var(--paper);
    overflow: hidden;
    box-shadow: 0 18px 40px rgba(80, 25, 10, 0.35);
  }
  .aura {
    position: absolute; inset: 0;
    background:
      radial-gradient(ellipse 150px 200px at 22% 30%, var(--pink), transparent 70%),
      radial-gradient(ellipse 170px 240px at 30% 72%, var(--rose), transparent 70%),
      radial-gradient(ellipse 200px 170px at 55% 24%, var(--lime), transparent 70%),
      radial-gradient(ellipse 150px 150px at 70% 16%, var(--sun), transparent 70%),
      radial-gradient(ellipse 120px 220px at 85% 42%, var(--amber), transparent 70%),
      radial-gradient(ellipse 150px 160px at 74% 66%, var(--sky), transparent 70%),
      radial-gradient(ellipse 140px 140px at 52% 76%, var(--lilac), transparent 70%);
    filter: blur(6px);
  }
  .mandala {
    position: absolute;
    left: 96px; top: 170px;
    width: 400px; height: 400px;
    border-radius: 50%;
    background: radial-gradient(circle, rgba(255,255,255,0.28), rgba(255,255,255,0.08) 60%, transparent 72%);
  }
  .title {
    position: absolute;
    left: 0; right: 0; top: 258px;
    color: var(--ink);
    text-align: center;
  }
  .title-word {
    display: block;
    font-family: "Playfair Display", serif;
    font-weight: 400;
    font-size: 104px;
    line-height: 0.9;
    letter-spacing: -2px;
    text-transform: lowercase;
  }
  .title-word--first { margin-left: -40px; }
  .title-word--second { margin-left: 70px; }
  .title-joiner {
    display: flex; align-items: center; justify-content: center;
    gap: 8px;
    margin: 2px 0 4px;
    font-family: "Inter", sans-serif;
    font-weight: 800;
    font-size: 14px;
    letter-spacing: 1px;
  }
  .title-joiner::before, .title-joiner::after {
    content: ""; width: 90px; height: 1.5px; background: var(--ink);
  }
  .title-tail {
    display: block;
    margin-top: 4px; margin-left: 250px;
    font-family: "Inter", sans-serif;
    font-weight: 800;
    font-size: 14px;
    letter-spacing: 1px;
  }
  .author {
    position: absolute;
    left: 0; right: 0; top: 712px;
    text-align: center;
    font-family: "Inter", sans-serif;
    font-weight: 800;
    font-size: 15px;
    letter-spacing: 0.5px;
    color: var(--ink);
    text-transform: uppercase;
  }
</style>
</head>
<body>
<main class="stage">
  <section class="cover">
    <div class="aura"></div>
    <div class="mandala" role="img" aria-label="Faint Sri Yantra mandala behind the title"></div>
    <h1 class="title">
      <span class="title-word title-word--first">Weaving</span>
      <span class="title-joiner">THE</span>
      <span class="title-word title-word--second">Silver</span>
      <span class="title-tail">RIVER</span>
    </h1>
    <p class="author">Dr. Marisol Kendrick</p>
  </section>
</main>
</body>
</html>
```